New LGBT Nightclub Crowdfunding Poster

We need it to read well for social media posts. All colors should look similar to Seattle’s Sports Teams color schemes.

The top should have: The logo prominently with the fans in the background photo. and then still center and important, "Coming soon!" "You can be part of the first in line for the amazing things happening". (The call to action is the purchase of these amazing deals for the first weekend open / passes. That should be clear).

```html
<!DOCTYPE html>
<html lang="en">
<head>
<meta charset="UTF-8">
<title>The Rally — Crowdfunding Levels</title>
<link href="https://fonts.googleapis.com/css2?family=Black+Ops+One&family=Raleway:wght@600;700;800;900&family=Russo+One&display=swap" rel="stylesheet">
<style>
  :root{
    --stage:#4a4a4c;
    --navy:#1f2a55;
    --navy-deep:#16204a;
    --ink:#23263a;
    --green:#6cb33f;
    --green-dark:#4f9a2a;
    --sky:#e6f4fb;
    --white:#ffffff;
  }
  *{box-sizing:border-box;margin:0;padding:0}
  html,body{width:1200px;height:1000px;overflow:hidden;background:var(--stage)}
  .poster{
    position:absolute;left:266px;top:68px;width:669px;height:864px;overflow:hidden;
    background:linear-gradient(180deg,var(--sky) 0%,#f3fafd 40%,#ffffff 100%);
  }
  .poster__backdrop{position:absolute;inset:0}
  .logo{position:absolute;left:229px;top:42px;width:210px;height:210px}
  .logo__photo{
    position:absolute;inset:0;border-radius:50%;
    background:radial-gradient(circle at 50% 40%,#5a6796 0%,#2e3a6c 45%,#c9d6ea 80%,rgba(230,240,250,0) 100%);
  }
  .logo__name{
    position:absolute;left:0;right:0;top:88px;text-align:center;
    font-family:'Russo One',sans-serif;font-size:26px;line-height:30px;color:var(--white);letter-spacing:1px;
  }
  .headline{
    position:absolute;left:0;right:0;top:248px;text-align:center;white-space:nowrap;
    font-family:'Black Ops One',sans-serif;font-size:66px;line-height:72px;letter-spacing:2px;color:var(--navy);
    text-shadow:
      3px 0 0 #fff,-3px 0 0 #fff,0 3px 0 #fff,0 -3px 0 #fff,
      2px 2px 0 #fff,-2px -2px 0 #fff,2px -2px 0 #fff,-2px 2px 0 #fff,
      5px 0 0 var(--navy),-5px 0 0 var(--navy),0 5px 0 var(--navy),0 -5px 0 var(--navy),
      4px 4px 0 var(--navy),-4px -4px 0 var(--navy),4px -4px 0 var(--navy),-4px 4px 0 var(--navy);
  }
  .tagline{
    position:absolute;left:58px;right:58px;top:328px;text-align:center;
    font-family:'Raleway',sans-serif;font-weight:900;font-size:20.5px;line-height:28px;color:var(--ink);text-transform:uppercase;
  }
  .levels-title{
    position:absolute;left:67px;top:395px;width:535px;height:50px;
    background:var(--white);border:3px solid var(--green);
    font-family:'Black Ops One',sans-serif;font-size:34px;line-height:44px;text-align:center;letter-spacing:1px;
    white-space:nowrap;overflow:hidden;color:var(--green);
    text-shadow:2px 2px 0 var(--green-dark);
  }
  .levels{position:absolute;left:104px;top:457px;width:480px;list-style:none}
  .level{
    display:flex;align-items:flex-start;gap:24px;height:47px;
    font-family:'Raleway',sans-serif;font-weight:600;font-size:13.4px;line-height:17px;color:var(--ink);
  }
  .level span{width:425px}
  .level--tall{height:63px}
  .level svg{flex:0 0 26px;margin-top:2px}
  .cta{
    position:absolute;left:0;right:0;top:772px;text-align:center;white-space:nowrap;
    font-family:'Raleway',sans-serif;font-weight:900;font-size:27px;color:var(--green-dark);
  }
  .footer{position:absolute;left:0;right:0;bottom:0;height:38px;background:var(--navy-deep)}
  .contact{position:absolute;top:810px;left:0;right:0;display:flex;justify-content:center;gap:12px}
  .contact__pill{
    display:flex;align-items:center;gap:10px;height:32px;padding:0 14px 0 6px;border-radius:16px;
    background:#2d5f9a;border:2px solid #5c8dc6;white-space:nowrap;
    font-family:'Russo One',sans-serif;font-style:italic;font-size:18px;color:var(--white);letter-spacing:1px;
  }
  .contact__icon{width:22px;height:22px;border-radius:50%;background:var(--navy-deep);display:flex;align-items:center;justify-content:center}
</style>
</head>
<body>
<main class="poster">
  <svg class="poster__backdrop" width="669" height="864" viewBox="0 0 669 864" aria-hidden="true">
    <defs>
      <linearGradient id="lowerSky" x1="0" y1="0" x2="1" y2="1">
        <stop offset="0" stop-color="#8fc0e3"/>
        <stop offset="0.45" stop-color="#cfe6f4"/>
        <stop offset="1" stop-color="#ffffff"/>
      </linearGradient>
    </defs>
    <path d="M95 0 C140 40 90 100 40 90 C0 80 -10 40 0 0Z" fill="#d4ecf8"/>
    <path d="M560 0 C600 60 669 70 669 120 L669 0Z" fill="#d9eef9"/>
    <path d="M75 10 C130 -10 160 60 120 110 C80 150 60 60 75 10Z" fill="none" stroke="#fff" stroke-width="2"/>
    <path d="M570 70 C610 50 650 90 640 150 C630 200 560 190 550 140 C540 100 545 80 570 70Z" fill="none" stroke="#fff" stroke-width="2"/>
    <path d="M0 335 C120 360 260 420 334 420 C430 420 540 385 669 365 L669 864 L0 864Z" fill="url(#lowerSky)"/>
    <g fill="none" stroke="#ffffff" stroke-opacity="0.7" stroke-width="2">
      <path d="M40 600 L200 760 L360 600 L200 440Z"/>
      <path d="M140 820 L300 660 L460 820"/>
      <path d="M0 520 L120 640 L0 760"/>
      <path d="M430 560 L560 690 L669 580"/>
    </g>
    <path d="M0 332 C120 355 260 415 334 415 C430 415 540 382 669 362" fill="none" stroke="var(--green)" stroke-width="12"/>
  </svg>

  <div class="logo">
    <div class="logo__photo" role="img" aria-label="Watercolor photo of cheering fans with raised arms"></div>
    <div class="logo__name">THE<br>RALLY</div>
  </div>

  <h1 class="headline">COMING SOON!</h1>
  <p class="tagline">You can be part of the first in line for the amazing things happening</p>

  <h2 class="levels-title">CROWDFUNDING LEVELS</h2>

  <ul class="levels">
    <li class="level"><svg width="26" height="26" viewBox="0 0 26 26"><circle cx="12" cy="14" r="10" fill="none" stroke="var(--navy)" stroke-width="2"/><path d="M7 13 L12 18 L23 5" fill="none" stroke="var(--navy)" stroke-width="2.4"/></svg><span>$25 Opening Fri or Sat night Glitter GA Ticket w/Drag Royale Megastar. M (only 100 Available Per Night)</span></li>
    <li class="level"><svg width="26" height="26" viewBox="0 0 26 26"><circle cx="12" cy="14" r="10" fill="none" stroke="var(--navy)" stroke-width="2"/><path d="M7 13 L12 18 L23 5" fill="none" stroke="var(--navy)" stroke-width="2.4"/></svg><span>$50 Opening Fri or Sat Night Glitter Third Tier Seating<br>(Only 60 Available Per Night)</span></li>
    <li class="level"><svg width="26" height="26" viewBox="0 0 26 26"><circle cx="12" cy="14" r="10" fill="none" stroke="var(--navy)" stroke-width="2"/><path d="M7 13 L12 18 L23 5" fill="none" stroke="var(--navy)" stroke-width="2.4"/></svg><span>$75 Opening Fri or Sat Night Glitter Middle Tier seating Ticket w/secret Drag Royale Megastar. (Only 60 Available Per Night)</span></li>
    <li class="level"><svg width="26" height="26" viewBox="0 0 26 26"><circle cx="12" cy="14" r="10" fill="none" stroke="var(--navy)" stroke-width="2"/><path d="M7 13 L12 18 L23 5" fill="none" stroke="var(--navy)" stroke-width="2.4"/></svg><span>$100 Opening Fri or Sat Night Glitter VIP Ticket w/secret Drag Royale Megastar. (Only 60 Available Per Night)</span></li>
    <li class="level level--tall"><svg width="26" height="26" viewBox="0 0 26 26"><circle cx="12" cy="14" r="10" fill="none" stroke="var(--navy)" stroke-width="2"/><path d="M7 13 L12 18 L23 5" fill="none" stroke="var(--navy)" stroke-width="2.4"/></svg><span>$500 The Rally Pass Skip the line and free cover for<br>6 months. Not including Brunch Shows and Special Events. Plus The Rally Merch (50 Available)</span></li>
    <li class="level level--tall"><svg width="26" height="26" viewBox="0 0 26 26"><circle cx="12" cy="14" r="10" fill="none" stroke="var(--navy)" stroke-width="2"/><path d="M7 13 L12 18 L23 5" fill="none" stroke="var(--navy)" stroke-width="2.4"/></svg><span>$1,000 The Rally Gold Pass. Skip the line and free<br>cover for the year. Not including Brunch Shows and Special Events Plus The Rally Merch. (100 Available)</span></li>
  </ul>

  <p class="cta">ASK ABOUT THE RALLY ELITE PASS</p>

  <footer class="footer"></footer>
  <div class="contact">
    <div class="contact__pill">
      <span class="contact__icon"><svg width="12" height="12" viewBox="0 0 24 24"><path d="M6 2 L10 2 L11 8 L8 10 C9 13 11 15 14 16 L16 13 L22 14 L22 18 C22 20 20 22 18 22 C9 21 3 15 2 6 C2 4 4 2 6 2Z" fill="#fff"/></svg></span>
      (555) 013-2470
    </div>
    <div class="contact__pill">
      <span class="contact__icon"><svg width="12" height="12" viewBox="0 0 24 24"><circle cx="12" cy="12" r="10" fill="none" stroke="#fff" stroke-width="2"/><ellipse cx="12" cy="12" rx="4.5" ry="10" fill="none" stroke="#fff" stroke-width="2"/><path d="M2 12 H22" stroke="#fff" stroke-width="2"/></svg></span>
      WWW.THERALLYCLUB.COM
    </div>
  </div>
</main>
</body>
</html>
```